Stationery modern simple design
Corporate Stationery
Project: Stationery modern simple design
Creative Brief
Simple
Faisal Alqurashi
General Manager
Sable Grid Company 3858 Nakheel Crest Rd Wardah Tower Riyadh 13847 Saudi Arabia
info@sablegrid.example
www.sablegrid.example
address will be not use in business card and will be used in any other Stationery Arabic Address: شركة سابل جريد ٣٨٥٨ طريق النخيل الأعلى الرياض ١٣٨٤٧ المملكة العربية السعودية
فيصل القرشي المدير العام infor@sablegrid.example +966117290813 +9665031476095

```html
<!DOCTYPE html>
<html lang="en">
<head>
<meta charset="utf-8">
<title>Sable Grid – Business Card</title>
<link rel="stylesheet" href="https://fonts.googleapis.com/css2?family=Montserrat:wght@500;600;700&family=Open+Sans:wght@400;600;700&family=Cairo:wght@400;600&display=swap">
<style>
  :root {
    --bg: #2b2d31;
    --blue: #1b8bd6;
    --blue-deep: #0c6db4;
    --ink: #4a4f55;
    --muted: #7d8389;
    --rule: #c9ced3;
    --paper: #ffffff;
  }
  * { margin: 0; padding: 0; box-sizing: border-box; }
  html, body { width: 1200px; height: 689px; overflow: hidden; }
  body {
    background: var(--bg);
    font-family: "Open Sans", sans-serif;
    position: relative;
  }
  .card {
    position: absolute;
    top: 196px;
    width: 520px;
    height: 297px;
    border-radius: 14px;
    overflow: hidden;
  }
  .card-front {
    left: 50px;
    background: linear-gradient(135deg, var(--blue) 0%, var(--blue-deep) 100%);
    display: flex;
    flex-direction: column;
    align-items: center;
    justify-content: center;
    gap: 18px;
  }
  .brand-mark {
    width: 46px; height: 46px;
    border: 5px solid var(--paper);
    border-radius: 4px;
  }
  .brand-name {
    font-family: "Montserrat", sans-serif;
    font-weight: 600;
    font-size: 30px;
    letter-spacing: 2px;
    color: var(--paper);
  }
  .card-back { left: 630px; background: var(--paper); }
  .back-brand {
    position: absolute;
    left: 30px; top: 100px;
    width: 230px;
    display: flex; flex-direction: column; align-items: center; gap: 14px;
  }
  .back-brand .brand-mark { border-color: var(--blue); width: 40px; height: 40px; }
  .back-brand .brand-name { color: var(--blue); font-size: 24px; }
  .divider {
    position: absolute; left: 272px; top: 60px;
    width: 1px; height: 170px; background: var(--rule);
  }
  .person { position: absolute; left: 290px; top: 34px; }
  .person-name { font-size: 18px; font-weight: 700; color: var(--blue); }
  .person-name-ar {
    font-family: "Cairo", sans-serif; font-weight: 600;
    font-size: 12px; color: var(--blue); direction: rtl; text-align: left;
  }
  .person-title { font-size: 10px; color: var(--muted); margin-top: 2px; }
  .contact {
    position: absolute; left: 290px; top: 128px;
    list-style: none; font-size: 10.5px; color: var(--ink); line-height: 1.5;
  }
  .contact li { display: flex; align-items: flex-start; gap: 8px; }
  .contact li + li { margin-top: 3px; }
  .contact svg { flex: none; margin-top: 2px; }
  .web-band {
    position: absolute; right: 0; bottom: 22px;
    width: 210px; height: 24px;
    background: var(--blue);
    clip-path: polygon(16px 0, 100% 0, 100% 100%, 0 100%);
    color: var(--paper);
    font-size: 11px; font-weight: 600;
    display: flex; align-items: center; justify-content: flex-end;
    padding-right: 18px;
  }
</style>
</head>
<body>
  <section class="card card-front">
    <div class="brand-mark"></div>
    <div class="brand-name">SABLE GRID</div>
  </section>

  <section class="card card-back">
    <div class="back-brand">
      <div class="brand-mark"></div>
      <div class="brand-name">SABLE GRID</div>
    </div>
    <div class="divider"></div>
    <div class="person">
      <div class="person-name">Faisal Alqurashi</div>
      <div class="person-name-ar">فيصل القرشي المدير العام</div>
      <div class="person-title">General Manager</div>
    </div>
    <ul class="contact">
      <li>
        <svg width="10" height="12" viewBox="0 0 10 12"><path d="M5 0a4 4 0 0 1 4 4c0 3-4 8-4 8S1 7 1 4a4 4 0 0 1 4-4z" fill="#1b8bd6"/><circle cx="5" cy="4" r="1.5" fill="#fff"/></svg>
        <span>3858 Nakheel Crest Rd<br>Wardah Tower Riyadh 13847<br>Saudi Arabia</span>
      </li>
      <li>
        <svg width="10" height="10" viewBox="0 0 10 10"><rect width="10" height="10" rx="2" fill="#1b8bd6"/><path d="M3 2.5l1.2 1.3-.6.8a5 5 0 0 0 1.8 1.8l.8-.6L7.5 7l-.8.8C4.5 7.6 2.4 5.5 2.2 3.3z" fill="#fff"/></svg>
        <span>+966117290813</span>
      </li>
      <li>
        <svg width="10" height="10" viewBox="0 0 10 10"><rect width="10" height="10" rx="2" fill="#1b8bd6"/><rect x="3" y="1.8" width="4" height="6.4" rx=".8" fill="#fff"/></svg>
        <span>+9665031476095</span>
      </li>
      <li>
        <svg width="10" height="10" viewBox="0 0 10 10"><rect width="10" height="10" rx="2" fill="#1b8bd6"/><path d="M2 3h6v4H2z M2 3l3 2.2L8 3" fill="none" stroke="#fff" stroke-width=".9"/></svg>
        <span>info@sablegrid.example</span>
      </li>
    </ul>
    <div class="web-band">www.sablegrid.example</div>
  </section>
</body>
</html>
```